K. Morendi needs an original business card for property investment professionals

The business card would be to present me as an investor in the real estate business. The market are developers of real estate projects, or other people who would like to sell and also to give us a name as a company. For style, colour and imagery I would like something artistic from Morendi (the artist) with a different touch.

Address, email, cel phone,
Updates

Hi¡ Update¡ I;d like it to stop providing Bright Acre as a Design and focus in K. Morendi.

Target Market(s)

Real Estate Developer/Investor

Industry/Entity Type

Real Estate

Colors
33a6d7
886aae
e3daeb
cadf82
f78f20

```html
<!DOCTYPE html>
<html lang="en">
<head>
<meta charset="utf-8">
<title>K. Morendi — Business Card</title>
<link rel="stylesheet" href="https://fonts.googleapis.com/css2?family=Tinos&display=swap">
<style>
  :root {
    --card-dark: #1f1f1f;
    --blue: #33a6d7;
    --purple: #886aae;
    --lavender: #e3daeb;
    --green: #cadf82;
    --orange: #f78f20;
    --white: #ffffff;
  }
  * { margin: 0; padding: 0; box-sizing: border-box; }
  html, body { width: 1200px; height: 1000px; overflow: hidden; background: var(--white); }
  .canvas { position: relative; width: 1200px; height: 1000px; }

  .card { position: absolute; background: var(--card-dark); overflow: hidden; }
  .card--front { left: 65px; top: 60px; width: 680px; height: 398px; }
  .card--back { left: 452px; top: 540px; width: 682px; height: 400px; }

  .pattern { position: absolute; display: block; }
  .pattern--corner-top { left: 0; top: 0; }
  .pattern--corner-bottom { right: 0; bottom: 0; }
  .pattern--band-top { left: 0; top: 0; }
  .pattern--band-bottom { left: 0; bottom: 0; }

  .brand-mark {
    position: absolute;
    display: flex; align-items: center; gap: 10px;
    font-family: "Tinos", serif; font-weight: 400;
    color: var(--lavender); white-space: nowrap;
  }
  .brand-mark__circle { width: 14px; height: 14px; border-radius: 50%; background: var(--blue); }
  .card--front .brand-mark { left: 80px; top: 180px; font-size: 28px; }
  .card--back .brand-mark { left: 252px; top: 182px; font-size: 32px; }

  .divider { position: absolute; left: 315px; top: 53px; width: 3px; height: 292px; background: var(--lavender); }

  .details { position: absolute; left: 360px; top: 64px; font-family: "Tinos", serif; color: var(--white); }
  .details__company { font-size: 38px; line-height: 52px; color: var(--purple); letter-spacing: 1px; }
  .details__name { font-size: 29px; line-height: 34px; color: var(--green); margin-top: 6px; }
  .details__contact, .details__office { font-size: 17px; line-height: 22px; }
  .details__contact { margin-top: 10px; }
  .details__office { margin-top: 21px; }
</style>
</head>
<body>
<div class="canvas">

  <section class="card card--front">
    <svg class="pattern pattern--corner-top" width="170" height="170" viewBox="0 0 170 170" role="img" aria-label="Stained-glass mosaic corner in blue, green, orange and purple">
      <defs>
        <linearGradient id="cornerTop" x1="0" y1="0" x2="1" y2="1">
          <stop offset="0" stop-color="#33a6d7"/>
          <stop offset="0.35" stop-color="#e3daeb"/>
          <stop offset="0.6" stop-color="#f78f20"/>
          <stop offset="0.85" stop-color="#886aae"/>
          <stop offset="1" stop-color="#cadf82"/>
        </linearGradient>
      </defs>
      <polygon points="0,0 168,0 0,168" fill="url(#cornerTop)"/>
    </svg>

    <div class="brand-mark"><span class="brand-mark__circle"></span>K. Morendi</div>

    <div class="divider"></div>

    <div class="details">
      <p class="details__company">K. Morendi</p>
      <p class="details__name">Lucia Arandes</p>
      <p class="details__contact">Cel.: 811-402-7315<br>E-mail: lucia.a@kmorendi.mx</p>
      <p class="details__office">Oficina: BRIGHT ACRE<br>Avenida Los Olmos 218<br>Local 9 Col. Las Lomas<br>Santa Clara RT, NL<br>66410 Mexico</p>
    </div>

    <svg class="pattern pattern--corner-bottom" width="166" height="166" viewBox="0 0 166 166" role="img" aria-label="Stained-glass mosaic corner in purple, lavender, blue, orange and green">
      <defs>
        <linearGradient id="cornerBottom" x1="1" y1="0" x2="0" y2="1">
          <stop offset="0" stop-color="#cadf82"/>
          <stop offset="0.3" stop-color="#886aae"/>
          <stop offset="0.55" stop-color="#e3daeb"/>
          <stop offset="0.75" stop-color="#33a6d7"/>
          <stop offset="1" stop-color="#f78f20"/>
        </linearGradient>
      </defs>
      <polygon points="166,0 166,166 0,166" fill="url(#cornerBottom)"/>
    </svg>
  </section>

  <section class="card card--back">
    <svg class="pattern pattern--band-top" width="682" height="37" viewBox="0 0 682 37" role="img" aria-label="Stained-glass mosaic band">
      <defs>
        <linearGradient id="bandTop" x1="0" y1="0" x2="1" y2="0">
          <stop offset="0" stop-color="#886aae"/>
          <stop offset="0.2" stop-color="#33a6d7"/>
          <stop offset="0.4" stop-color="#886aae"/>
          <stop offset="0.6" stop-color="#cadf82"/>
          <stop offset="0.8" stop-color="#886aae"/>
          <stop offset="1" stop-color="#33a6d7"/>
        </linearGradient>
      </defs>
      <rect width="682" height="37" fill="url(#bandTop)"/>
    </svg>

    <div class="brand-mark"><span class="brand-mark__circle"></span>K. Morendi</div>

    <svg class="pattern pattern--band-bottom" width="682" height="40" viewBox="0 0 682 40" role="img" aria-label="Stained-glass mosaic band">
      <defs>
        <linearGradient id="bandBottom" x1="0" y1="0" x2="1" y2="0">
          <stop offset="0" stop-color="#33a6d7"/>
          <stop offset="0.2" stop-color="#886aae"/>
          <stop offset="0.4" stop-color="#33a6d7"/>
          <stop offset="0.55" stop-color="#f78f20"/>
          <stop offset="0.75" stop-color="#886aae"/>
          <stop offset="0.9" stop-color="#e3daeb"/>
          <stop offset="1" stop-color="#cadf82"/>
        </linearGradient>
      </defs>
      <rect width="682" height="40" fill="url(#bandBottom)"/>
    </svg>
  </section>

</div>
</body>
</html>
```